Edit and Update existing catalog

I have a 60 paged catalog that needs to have some changes. We are adding around 20 pages, changing another 15 pages, and also have 10 pages that need to be graphically designed and inserted. The current existing catalog is included as well as a PDF explaining all the changes (Catalog Changes.pdf), as well as all the pages that need to be added and our logo.

Target Market(s)

physician offices and professional healthcare providers

Industry/Entity Type

Healthcare

Colors
0054AA
0677BA
7BADD7
CADEEF
E8F1F8

Requirements
Must have
• Additional pages must match the format of the existing catalog
Should not have
• No protected health information - all patient names, Date of births and accession #s should be removed, incase they are not please replace with XXX on the reports.

```html
<!DOCTYPE html>
<html lang="en">
<head>
<meta charset="utf-8">
<title>Toxicology – Catalog Section Cover</title>
<link href="https://fonts.googleapis.com/css2?family=Montserrat:wght@600;700;800&display=swap" rel="stylesheet">
<style>
  :root {
    --blue-primary: #1a73b8;
    --blue-deep: #0054aa;
    --charcoal: #4a4b4d;
    --text-gray: #555658;
    --white: #ffffff;
    --photo-light: #f3f5f7;
    --photo-mid: #dde3e9;
  }
  html, body {
    margin: 0;
    padding: 0;
    width: 982px;
    height: 1200px;
    overflow: hidden;
    background: var(--white);
  }
  .page {
    position: relative;
    width: 982px;
    height: 1200px;
    overflow: hidden;
    background: var(--white);
    font-family: "Montserrat", Arial, sans-serif;
  }
  .page-shapes {
    position: absolute;
    inset: 0;
  }
  .cover-photo {
    position: absolute;
    left: 0;
    top: 560px;
    width: 914px;
    height: 640px;
    background: linear-gradient(160deg, var(--photo-light) 0%, var(--photo-mid) 100%);
  }
  .brand {
    position: absolute;
    left: 106px;
    top: 112px;
    display: flex;
    align-items: center;
    gap: 18px;
  }
  .brand-mark {
    width: 70px;
    height: 70px;
    border: 6px solid var(--white);
    border-radius: 50%;
    box-sizing: border-box;
  }
  .brand-name {
    color: var(--white);
    font-weight: 700;
    font-size: 30px;
    letter-spacing: 0.5px;
  }
  .section-heading {
    position: absolute;
    left: 130px;
    top: 438px;
  }
  .section-title {
    margin: 0;
    color: var(--blue-primary);
    font-weight: 800;
    font-size: 62px;
    line-height: 1;
    letter-spacing: 0.5px;
  }
  .section-subtitle {
    margin: 16px 0 0 2px;
    color: var(--text-gray);
    font-weight: 700;
    font-size: 19.5px;
    letter-spacing: 0.6px;
  }
  .side-tab-label {
    position: absolute;
    left: 948px;
    color: var(--white);
    font-weight: 600;
    font-size: 17px;
    white-space: nowrap;
    transform: translate(-50%, -50%) rotate(90deg);
  }
  .side-tab-label.is-section { top: 250px; }
  .side-tab-label.is-trim { top: 700px; }
  .page-number {
    position: absolute;
    left: 876px;
    top: 1162px;
    color: var(--white);
    font-weight: 600;
    font-size: 15px;
  }
</style>
</head>
<body>
  <div class="page">
    <div class="cover-photo" role="img" aria-label="Photo of a smiling physician in a white coat showing a tablet to a laughing patient in a bright clinic"></div>

    <svg class="page-shapes" width="982" height="1200" viewBox="0 0 982 1200" aria-hidden="true">
      <polygon fill="var(--white)" points="0,540 914,190 914,0 0,0"/>
      <polygon fill="var(--blue-primary)" points="0,0 914,0 914,14 0,438"/>
      <polygon fill="var(--charcoal)" points="0,452 914,28 914,66 0,492"/>
      <rect fill="var(--blue-primary)" x="914" y="0" width="68" height="375"/>
      <rect fill="var(--charcoal)" x="914" y="375" width="68" height="825"/>
      <polygon fill="var(--white)" points="120,1200 914,1058 914,1070 160,1200"/>
      <polygon fill="var(--blue-primary)" points="150,1200 914,1066 982,1060 982,1200"/>
    </svg>

    <div class="brand">
      <span class="brand-mark"></span>
      <span class="brand-name">Northvale Labs</span>
    </div>

    <div class="section-heading">
      <h1 class="section-title">Toxicology</h1>
      <p class="section-subtitle">URINE AND ORAL FLUID DRUG TESTING</p>
    </div>

    <span class="side-tab-label is-section">Toxicology</span>
    <span class="side-tab-label is-trim">Trim Area</span>

    <span class="page-number">3</span>
  </div>
</body>
</html>
```